Visitenkarten-Design
Zielgruppe
Malerbetrieb
Zielgruppe: Private Haushalte, Hausverwaltungen
Aufgabenstellung
Logo ist vorhanden
Lorenz Dallmer
Malermeister

```html
<!DOCTYPE html>
<html lang="de">
<head>
<meta charset="utf-8">
<title>Visitenkarte – Malereibetrieb Dallmer</title>
<link href="https://fonts.googleapis.com/css2?family=Fira+Sans:wght@300;400;600&family=Open+Sans:wght@400&display=swap" rel="stylesheet">
<style>
  :root {
    --stage: #cfcfcf;
    --card: #ffffff;
    --frame: #009fe0;
    --ink: #202428;
    --muted: #9a9a9a;
  }
  html, body {
    margin: 0;
    padding: 0;
    width: 1200px;
    height: 849px;
    overflow: hidden;
    background: var(--stage);
  }
  .stage {
    position: relative;
    width: 1200px;
    height: 849px;
  }
  .card {
    position: absolute;
    top: 281px;
    width: 445px;
    height: 288px;
    box-sizing: border-box;
    border: 9px solid var(--frame);
    background: var(--card);
    font-family: "Fira Sans", sans-serif;
    color: var(--ink);
  }
  .card--front { left: 90px; }
  .card--back { left: 671px; }

  .wordmark {
    position: absolute;
    margin: 0;
    font-family: "Fira Sans", sans-serif;
    font-weight: 600;
    color: var(--ink);
    line-height: 1;
    white-space: nowrap;
  }
  .trade {
    position: absolute;
    margin: 0;
    font-family: "Fira Sans", sans-serif;
    font-weight: 300;
    color: var(--ink);
    line-height: 1;
    white-space: nowrap;
  }

  .card--front .wordmark {
    left: 0;
    right: 0;
    top: 62px;
    text-align: center;
    font-size: 68px;
    letter-spacing: 3px;
  }
  .card--front .trade {
    left: 0;
    right: 0;
    top: 146px;
    text-align: center;
    font-size: 35px;
    letter-spacing: 0.5px;
  }
  .tagline {
    position: absolute;
    left: 0;
    right: 0;
    top: 181px;
    margin: 0;
    text-align: center;
    font-family: "Open Sans", sans-serif;
    font-size: 18.5px;
    color: var(--muted);
  }

  .card--back .wordmark {
    right: 25px;
    top: 21px;
    text-align: right;
    font-size: 31px;
    letter-spacing: 1px;
  }
  .card--back .trade {
    right: 25px;
    top: 61px;
    text-align: right;
    font-size: 16px;
    letter-spacing: 0;
  }

  .contact {
    position: absolute;
    left: 21px;
    top: 111px;
    margin: 0;
    font-size: 16px;
    line-height: 20.5px;
    font-style: normal;
  }
  .contact__name { font-weight: 600; display: block; }
  .contact__role { display: block; }
  .contact__lines { display: block; margin-top: 20px; }
  .contact__web { display: block; font-weight: 600; margin-top: 18px; }
</style>
</head>
<body>
<main class="stage">
  <section class="card card--front" aria-label="Vorderseite">
    <p class="wordmark">DALLMER</p>
    <p class="trade">MALEREIBETRIEB</p>
    <p class="tagline">Sorgfalt in jeder Farbe und Fläche</p>
  </section>

  <section class="card card--back" aria-label="Rückseite">
    <p class="wordmark">DALLMER</p>
    <p class="trade">MALEREIBETRIEB</p>
    <address class="contact">
      <span class="contact__name">Lorenz Dallmer</span>
      <span class="contact__role">Malermeister</span>
      <span class="contact__lines">Lindenkamp 48 b | 22147 Hamburg<br>Tel: 0172-5408213 | info@malereibetrieb-dallmer.de</span>
      <span class="contact__web">www.malereibetrieb-dallmer.de</span>
    </address>
  </section>
</main>
</body>
</html>
```